Curtain and Blind Manufacturers - Retail Ecommerce All Pages

To Design a high converting website design for and improve on the domain www.velcourt-weaves.co.uk.

Generally it is improvements on what already exists, the core layout is functional and strong. Needs to have the header mobile responsive. Core elements for each page and clear content.

Current header is good just needs modernising and needs to work well on mobile. Need a way of having a mixture of categories and advice where necessary.

Pages and detailing required.
Home - Great Imagery for the sections. Category specific. A good product offering. So Call to product. Potentially straight to our best selling products. Not in a slider but in a straight forward grid. A nice simlar design to competitors in my space. shutterly4u, my own website. also i like websites like nessa mattresses, harrowdens.co.uk needs to be simple with clear direction for the customer particularly on mobile to get them to what we do quickly. EG curtains, blinds etc

Inner pages

Category Top Filters
https://www.velcourt-weaves.co.uk/flame-retardant/curtains

Category Side bar filters

Category Mobile with Off Canvas Filters

Product - Fabric
https://www.velcourt-weaves.co.uk/tovra-flame-retardant-curtain-fabric.html

Product - Curtains - https://www.velcourt-weaves.co.uk/tovra-fr-curtains.html

Product - Blinds
Cart
Checkout
Slide in Cart
Slide in Filters
General Content Page
About

```html
<!DOCTYPE html>
<html lang="en">
<head>
<meta charset="utf-8">
<title>Velcourt Weaves – Curtains, Blinds, Fabric</title>
<link href="https://fonts.googleapis.com/css2?family=Poppins:wght@400;500;600;700&display=swap" rel="stylesheet">
<style>
:root{
  --red:#d0202e;
  --red-dark:#a8141f;
  --ink:#1d1d1d;
  --text:#555;
  --muted:#888;
  --line:#e3e3e3;
  --grey-bg:#f1f1f1;
  --soft:#f5f5f5;
  --white:#fff;
  --star:#f3b51b;
  --dark:#2a1410;
}
*{box-sizing:border-box;margin:0;padding:0}
html,body{width:1200px;height:4246px;overflow:hidden}
body{font-family:'Poppins',sans-serif;color:var(--ink);background:var(--white);font-size:11px}
.wrap{width:876px;margin:0 auto;position:relative;height:100%}
a{color:inherit;text-decoration:none}
.btn{display:inline-block;border-radius:20px;font-weight:600;font-size:9px;letter-spacing:.5px;text-transform:uppercase;padding:9px 22px}
.btn-red{background:var(--red);color:#fff}
.btn-outline{border:1.5px solid var(--red);color:var(--red);background:#fff}
.section-title{font-size:22px;font-weight:600;text-align:center}

/* top bar */
.topbar{height:26px;border-bottom:1px solid var(--line);font-size:7.5px;color:#444}
.topbar .wrap{display:flex;align-items:center;justify-content:space-between}
.pay{display:flex;gap:8px;align-items:center}
.pay span{font-weight:700;font-size:7.5px}
.rating-mini{display:flex;align-items:center;gap:4px;font-weight:600}
.stars{color:var(--star);letter-spacing:1px}

/* header */
.header{height:60px}
.header .wrap{display:flex;align-items:center}
.logo{display:flex;align-items:center;gap:8px}
.logo-mark{width:30px;height:30px;background:var(--red)}
.logo-name{font-weight:700;font-size:17px;color:var(--red);line-height:1}
.search{margin-left:auto;width:260px;height:28px;border:1px solid var(--line);border-radius:16px;display:flex;align-items:center;justify-content:space-between;padding:0 12px;color:#aaa;font-size:8px}
.head-btns{display:flex;gap:8px;margin-left:14px;align-items:center}
.icon-circle{width:26px;height:26px;border:1px solid var(--red);border-radius:50%;display:flex;align-items:center;justify-content:center}

/* nav */
.nav{height:33px;background:var(--red);color:#fff}
.nav ul{list-style:none;display:flex;height:33px;align-items:center;gap:18px;font-size:9px;font-weight:500;text-transform:uppercase}
.nav li.active{border-bottom:2px solid #fff;padding-bottom:3px}

/* hero */
.hero{height:438px;position:relative;background:linear-gradient(120deg,#3a1a16 0%,#8a2f22 30%,#c14a2d 50%,#7a2a1f 70%,#3c1b18 100%)}
.hero-copy{position:absolute;left:0;top:145px;color:#fff;width:520px}
.hero-copy h1{font-size:22px;font-weight:600;line-height:1.45}
.hero-copy .btn{margin-top:20px;font-size:8px}
.quote-box{position:absolute;right:0;top:57px;width:249px;height:335px;background:#fff;padding:22px 20px;text-align:center}
.quote-box h3{font-size:13px;font-weight:600;line-height:1.35}
.quote-box h3 em{color:var(--red);font-style:normal}
.quote-box p{font-size:8px;color:#444;margin:10px 0 12px;line-height:1.5}
.field{height:22px;background:var(--soft);border-radius:12px;margin-bottom:9px;text-align:left;padding:0 12px;font-size:8px;color:#999;display:flex;align-items:center}
.field.tall{height:56px;align-items:flex-start;padding-top:7px;border-radius:10px}

/* trusted */
.trusted{height:74px;background:var(--grey-bg)}
.trusted .wrap{display:flex;align-items:center;justify-content:space-between}
.trusted h4{font-size:12px;font-weight:600}
.partner{width:148px;height:48px;background:#fff;display:flex;align-items:center;justify-content:center;font-size:15px;font-weight:600;color:#444}

/* categories */
.cats{height:794px;padding-top:48px}
.cat-grid{display:grid;grid-template-columns:repeat(4,206px);gap:18px;justify-content:space-between;margin-top:22px}
.cat{height:205px;display:flex;align-items:center;justify-content:center;text-align:center;color:#fff;font-weight:700;font-size:13px;line-height:1.3;padding:0 20px;text-transform:uppercase;text-shadow:0 1px 3px rgba(0,0,0,.4)}

/* about band */
.band{height:371px;background:linear-gradient(115deg,#1c4a4a 0%,#5a1b4a 30%,#b02a3a 55%,#c4722a 75%,#2a3a6a 100%);color:#fff;text-align:center;padding-top:42px}
.band h2{font-size:22px;font-weight:600;margin-bottom:18px}
.band p{font-size:10px;line-height:1.65;margin-bottom:16px;padding:0 10px}
.band b{font-weight:600}
.band .red{color:#ff5561}

/* reviews */
.reviews{height:198px}
.reviews .wrap{display:flex;padding-top:50px}
.rev-sum{width:225px}
.rev-sum h4{font-size:12px;font-weight:600}
.rev-sum .big{font-size:18px;margin:6px 0}
.rev-sum small{font-size:7px;color:#444}
.rev-sum small u{color:var(--red)}
.brand{font-weight:600;font-size:11px;margin-top:14px;display:flex;align-items:center;gap:5px}
.brand i{width:9px;height:9px;background:#1b9c64;display:inline-block}
.rev{width:217px;padding-right:20px}
.rev .head{font-size:7px;color:var(--muted)}
.rev h5{font-size:9.5px;font-weight:600;margin:10px 0 6px}
.rev p{font-size:8px;color:var(--text);line-height:1.55}
.rev .who{font-size:8px;margin-top:8px;color:#333}
.rev .who b{font-weight:600}

/* specialists */
.spec{height:552px;background:var(--grey-bg);padding-top:44px}
.spec .intro{font-size:9.5px;line-height:1.65;text-align:center;color:#333;margin:14px 0 22px}
.spec .intro b{font-weight:600}
.spec-grid{display:grid;grid-template-columns:repeat(4,206px);justify-content:space-between}
.spec-card{text-align:center}
.spec-img{height:173px}
.spec-card h4{font-size:12px;font-weight:600;margin:18px 0 8px;text-transform:uppercase}
.spec-card p{font-size:8.5px;color:var(--text);line-height:1.6;padding:0 4px;height:92px}
.arrow{width:28px;height:28px;border-radius:50%;border:1px solid #ccc;display:inline-flex;align-items:center;justify-content:center;margin-top:12px;background:#fff}
.arrow.on{background:var(--red);border-color:var(--red)}

/* favourites */
.fav{height:495px;padding-top:44px}
.prod-grid{display:grid;grid-template-columns:repeat(4,206px);justify-content:space-between;margin-top:18px}
.prod{border:1px solid var(--line);height:309px;text-align:center}
.prod-img{height:173px}
.prod h5{font-size:10px;font-weight:500;line-height:1.5;margin:14px 10px 4px;height:32px}
.prod .stars{font-size:11px}
.price{display:flex;justify-content:space-between;font-size:8px;color:#444;margin:10px 14px}
.actions{display:flex;justify-content:space-between;font-size:6.5px;font-weight:600;margin:14px 14px 0;text-transform:uppercase}
.actions span:first-child{color:var(--red)}
.fav-btns{text-align:center;margin-top:22px}
.fav-btns .btn{margin:0 4px}

/* blog */
.blog{height:453px;position:relative;background:linear-gradient(90deg,#d9cbb8 0%,#b58a6a 18%,#efe8de 50%,#cdbfae 80%,#9a6a4c 100%)}
.blog h2{text-align:center;font-size:22px;font-weight:600;padding-top:44px}
.blog-grid{position:absolute;left:274px;top:85px;display:flex;gap:20px}
.post{width:204px;height:269px;background:#fff;text-align:center}
.post-img{height:172px}
.post h5{font-size:10px;font-weight:500;line-height:1.5;margin:14px 14px 6px}
.post h5.red{color:var(--red)}
.post small{font-size:6.5px;color:var(--red)}
.blog .next{position:absolute;left:941px;top:208px;width:24px;height:24px;border-radius:50%;background:var(--red);display:flex;align-items:center;justify-content:center}
.blog .btn{position:absolute;left:580px;top:382px}

/* faq & contact */
.faq{height:412px}
.faq .wrap{display:flex;justify-content:space-between;padding-top:44px}
.faq-col{width:415px}
.faq h2,.contact h2{font-size:22px;font-weight:600;margin-bottom:20px}
.q{border-bottom:1px solid var(--line);padding:10px 8px;font-size:8.5px;font-weight:500;display:flex;justify-content:space-between;text-transform:uppercase}
.q b{color:var(--red);font-weight:400;font-size:13px;line-height:8px}
.q.open{color:var(--red);border-bottom:none}
.answer{font-size:8.5px;color:var(--text);line-height:1.6;padding:0 10px 12px;border-bottom:1px solid var(--line)}
.faq .btn{margin-top:24px}
.contact{width:350px}
.contact .field{height:24px;margin-bottom:11px}
.contact .field.tall{height:60px}
.agree{font-size:8px;display:flex;align-items:center;gap:8px;margin:10px 0 14px}
.agree i{width:12px;height:12px;border:1px solid var(--red);display:inline-block}
.agree u{color:var(--red)}

/* footer */
.footer{height:340px;background:linear-gradient(100deg,#1e0d0a 0%,#4a1a12 45%,#2a100c 100%);color:#fff;position:relative}
.foot-cols{display:flex;padding-top:44px}
.fcol{width:224px;font-size:8.5px}
.fcol h4{font-size:13px;font-weight:600;margin-bottom:16px;text-transform:uppercase}
.fcol ul{list-style:none;line-height:2.35}
.fcol li.red{color:var(--red)}
.ci{display:flex;gap:14px;align-items:flex-start;margin-bottom:14px;line-height:1.55}
.ci .ic{width:22px;height:22px;border:1px solid rgba(255,255,255,.5);border-radius:50%;flex:none;display:flex;align-items:center;justify-content:center}
.ci .red{color:var(--red)}
.foot-logo{background:#fff;padding:10px 12px;display:inline-flex;align-items:center;gap:8px}
.social{display:flex;gap:8px;margin:10px 0 18px}
.social i{width:22px;height:22px;border:1px solid rgba(255,255,255,.6);border-radius:50%;display:inline-block}
.social i.on{background:var(--red);border-color:var(--red)}
.bottom{position:absolute;left:0;right:0;bottom:0;height:34px;border-top:1px solid rgba(255,255,255,.15);font-size:7.5px}
.bottom .wrap{display:flex;align-items:center;justify-content:space-between}
.bottom .red{color:var(--red)}
.cards{display:flex;gap:4px}
.cards span{background:#fff;color:#333;font-size:6px;font-weight:600;padding:2px 4px;border-radius:2px}
</style>
</head>
<body>

<div class="topbar"><div class="wrap">
  <div class="pay"><span>PayWay</span><span>Cardia</span><span>Mastro</span><span style="font-weight:500">FREE DELIVERY £250 UK EX SH&amp;I</span></div>
  <div class="rating-mini"><span class="stars">★★★★★</span>Revuely</div>
  <div>FREE FABRIC SAMPLES &nbsp;|&nbsp; NATIONWIDE INSTALLATION &nbsp;|&nbsp; CONTACT US</div>
</div></div>

<header class="header"><div class="wrap">
  <a class="logo" href="#"><span class="logo-mark"></span><span class="logo-name">Velcourt Weaves</span></a>
  <div class="search">Search Entire Store Here...
    <svg width="10" height="10" viewBox="0 0 10 10"><circle cx="4" cy="4" r="3" fill="none" stroke="#555"/><path d="M6.3 6.3 9 9" stroke="#555"/></svg></div>
  <div class="head-btns">
    <a class="btn btn-outline" style="font-size:8px;padding:7px 16px">Call Now!</a>
    <a class="btn btn-red" style="font-size:8px;padding:7px 16px">Get Quick Quote!</a>
    <span class="icon-circle"><svg width="12" height="12" viewBox="0 0 12 12"><circle cx="6" cy="4" r="2.3" fill="none" stroke="#d0202e"/><path d="M2 11c0-2.5 2-4 4-4s4 1.5 4 4" fill="none" stroke="#d0202e"/></svg></span>
    <span class="icon-circle"><svg width="12" height="12" viewBox="0 0 12 12"><path d="M1 2h2l1.5 6h5.5l1-4.5H4" fill="none" stroke="#d0202e"/><circle cx="5" cy="10.3" r=".9" fill="#d0202e"/><circle cx="9" cy="10.3" r=".9" fill="#d0202e"/></svg></span>
  </div>
</div></header>

<nav class="nav"><div class="wrap"><ul>
  <li class="active">Home</li><li>About Us</li><li>Curtains ▾</li><li>Blinds ▾</li><li>Fabrics ▾</li><li>Flame Retardant ▾</li><li>Tracks ▾</li><li>Poles ▾</li><li>Bedding &amp; Linens ▾</li><li>Furniture ▾</li><li>FAQ's</li><li>Blog</li>
</ul></div></nav>

<section class="hero" role="img" aria-label="Close-up of rolled, colourful woven fabric bolts">
  <div class="wrap">
    <div class="hero-copy">
      <h1>Flame Retardant &amp; Contract Specialists.<br>Contact today - Supply Only OR Manufacture to Installation</h1>
      <a class="btn btn-red">Shop Online for Contract Furnishings</a>
    </div>
    <form class="quote-box">
      <h3>Quick Quote &amp;<br><em>Free</em> Sample Requests</h3>
      <p><b>SAVE TIME</b> - Send your project requirements, large or small. Sample Lists etc</p>
      <div class="field">Your Name</div>
      <div class="field">Your Email</div>
      <div class="field">Phone Number</div>
      <div class="field tall">Message...</div>
      <a class="btn btn-red" style="margin-top:6px;font-size:8px">Send Message Now</a>
    </form>
  </div>
</section>

<section class="trusted"><div class="wrap">
  <h4>SUPPLYING &amp; TRUSTED BY</h4>
  <div class="partner">Aerohaven</div>
  <div class="partner">Restwell Inn</div>
  <div class="partner">Carewell Health</div>
  <div class="partner">Tally&amp;Co</div>
</div></section>

<section class="cats"><div class="wrap">
  <h2 class="section-title">Shop by Categories</h2>
  <div class="cat-grid">
    <div class="cat" role="img" aria-label="Deep red curtains" style="background:linear-gradient(90deg,#4a0d18,#8a1a2c,#5a1020)">Shop Curtains</div>
    <div class="cat" role="img" aria-label="Colourful draped fabrics" style="background:linear-gradient(135deg,#1a6a7a,#b02a5a,#d0702a)">Shop Fabrics</div>
    <div class="cat" role="img" aria-label="Wooden slat blinds" style="background:linear-gradient(180deg,#6a4a34,#3a2418,#7a5238)">Shop Blinds</div>
    <div class="cat" role="img" aria-label="Dark curtains framing a window" style="background:linear-gradient(90deg,#1e1e1e,#3e4a34,#1e1e1e)">Flame Retardant Curtains</div>
    <div class="cat" role="img" aria-label="Theatre stage curtains" style="background:linear-gradient(180deg,#2a0a14,#7a1226,#3a2a2a)">Stage / Theatre Curtains</div>
    <div class="cat" role="img" aria-label="Bedding in a warm lit room" style="background:linear-gradient(135deg,#c07a2a,#6a3a1a,#2a1a14)">Flame Retardant Bedding</div>
    <div class="cat" role="img" aria-label="Red curtain fabric folds" style="background:linear-gradient(90deg,#8a1a24,#c43040,#8a1a24)">Fire Resistant Curtain Fabrics</div>
    <div class="cat" role="img" aria-label="Grey roller blind at a window" style="background:linear-gradient(180deg,#9aa0a4,#6e7478)">Fire Retardant Roller Blinds</div>
    <div class="cat" role="img" aria-label="Cream cubicle curtains" style="background:linear-gradient(90deg,#c8b08a,#a88a60)">Cubicle Curtains and Tracks</div>
    <div class="cat" role="img" aria-label="Curtain track rails" style="background:linear-gradient(180deg,#8a8a84,#4a4a46,#9a9088)">Curtain Tracks</div>
    <div class="cat" role="img" aria-label="Metal venetian blinds" style="background:linear-gradient(90deg,#4a1a1a,#7a3a34,#3a1614)">Metal Venetian Blinds</div>
    <div class="cat" role="img" aria-label="Vertical blinds" style="background:linear-gradient(90deg,#8a8884,#c4c0b8,#6a6660)">Vertical Blinds</div>
  </div>
</div></section>

<section class="band" role="img" aria-label="Flowing multicoloured silk fabric"><div class="wrap">
  <h2>Velcourt Weaves - Curtains, Blinds, Fabric</h2>
  <p>Velcourt Weaves has been set up to supply the UK and the world with a superior range of <b>curtain fabrics</b> and <b>made to measure curtains</b>. Ensuring that all products are certified to the necessary British and European flame retardant standards. Our flame retardant fabrics are manufactured into excellent curtains, blinds and soft furnishings in our factories across the UK. Purchase your <b>contract curtains</b> and soft furnishings from a UK company with a large buying power that can offer the full service from design, manufacture and installation of contract furnishings. The team at Velcourt Weaves will ensure that you can get the project completed on time and on budget with made to measure curtains manufactured in as little as <b>15-20 working days.</b></p>
  <p>The products Velcourt Weaves offer to the health service include hospital <span class="red">cubicle curtain rails, cubicle curtains</span>. The team will work with you to get the very commercial certified flame retardant products for your business.</p>
  <p>Velcourt Weaves supply businesses from all sectors including; <b>Care, Hospitality and Education</b>. Working with at risk areas within care homes and schools, Velcourt Weaves understand the risks and ensure that the products are all ideally suited both in design and in performance. Buy from a UK business that can deliver quickly and with excellent quality <b>contract furnishings</b>.</p>
</div></section>

<section class="reviews"><div class="wrap">
  <div class="rev-sum">
    <h4>EXCELLENT</h4>
    <div class="big stars">★★★★★</div>
    <small>Based on <u>1,675 reviews</u></small>
    <div class="brand"><i></i>Revuely</div>
  </div>
  <div class="rev"><div class="head"><span class="stars">★★★★★</span> Verified</div>
    <h5>The agent I spoke to in an online chat...</h5>
    <p>The agent I spoke to in an online chat was very helpful, answering all my questions...</p>
    <div class="who"><b>- JUNE,</b> 6 days ago</div></div>
  <div class="rev"><div class="head"><span class="stars">★★★★★</span> Verified</div>
    <h5>Great product, very reasonable price.</h5>
    <p>The curtain track arrived quickly and was great quality despite the very reasona...</p>
    <div class="who"><b>- RBAILEY,</b> 3 days ago</div></div>
  <div class="rev"><div class="head"><span class="stars">★★★★★</span> Verified</div>
    <h5>Good quality</h5>
    <p>Great response, quickly delivery, fab quality of the fabric.</p>
    <div class="who"><b>- MARISOL,</b> 2 days ago</div></div>
</div></section>

<section class="spec"><div class="wrap">
  <h2 class="section-title">Flame Retardant &amp; Contract Furnishing Specialists</h2>
  <p class="intro">Velcourt Weaves supply the UK with soft furnishings for commercial environments certified to <b>British and International Flame Retardant Standards</b>. Including BS5867, BS7175, BS5852, IMO MI &amp; B1. Velcourt Weaves has been set up to supply the UK and the world with a superior range of contract furnishings. From manufacture to installation. We are an approved health service supplier and work supplying hotels, care homes, schools and more. Our company is based in the United Kingdom. We look forward to working with you to supply the very <b>best contract curtains, blinds, stage curtains and also cubicle curtains and tracks.</b></p>
  <div class="spec-grid">
    <div class="spec-card"><div class="spec-img" role="img" aria-label="Sewing machine in a UK workshop" style="background:linear-gradient(135deg,#3a3a3a,#8a8a88,#2a2a2a)"></div>
      <h4>UK Manufactured</h4><p>All our curtains and blinds are made here in the United Kingdom. We believe in quality and buying British where possible, so we make all of our made to measure soft furnishings including; curtains, blinds, accessories here in the UK.</p>
      <span class="arrow"><svg width="10" height="8" viewBox="0 0 10 8"><path d="M0 4h9M6 1l3 3-3 3" fill="none" stroke="#333"/></svg></span></div>
    <div class="spec-card"><div class="spec-img" role="img" aria-label="Health service supplier badge" style="background:#0a5ab8"></div>
      <h4>Certified Health Supplier</h4><p>Velcourt Weaves are registered health service suppliers working on small projects for individual medical practices as well as full <b>hospital</b> contract for cubicle curtain rails</p>
      <span class="arrow on"><svg width="10" height="8" viewBox="0 0 10 8"><path d="M0 4h9M6 1l3 3-3 3" fill="none" stroke="#fff"/></svg></span></div>
    <div class="spec-card"><div class="spec-img" role="img" aria-label="Green cassette roller blind on a window" style="background:linear-gradient(180deg,#c8ccc0,#a8b49a,#e0e0da)"></div>
      <h4>Cassettte Roller Blinds</h4><p>A <b>cassette blackout roller blind</b> manufacturer who manufactures the very best roller blinds for commercial and domestic situations. Our cassette roller blinds are one of the highest quality and made to last with a 10 year guarantee...</p>
      <span class="arrow"><svg width="10" height="8" viewBox="0 0 10 8"><path d="M0 4h9M6 1l3 3-3 3" fill="none" stroke="#333"/></svg></span></div>
    <div class="spec-card"><div class="spec-img" role="img" aria-label="Hotel room with purple soundproof curtains" style="background:linear-gradient(135deg,#2a1a3a,#6a3a6a,#a05a4a)"></div>
      <h4>Soundproof Curtains</h4><p>A <b>Soundproof curtain</b> manufacturer. We only use certified and tested products that deliver the highest acoustic absorption with an 11db sound proofing. All tested and certified products that work to soundproof your rooms with curtains...</p>
      <span class="arrow"><svg width="10" height="8" viewBox="0 0 10 8"><path d="M0 4h9M6 1l3 3-3 3" fill="none" stroke="#333"/></svg></span></div>
  </div>
</div></section>

<section class="fav"><div class="wrap">
  <h2 class="section-title">Some of Our Favourites</h2>
  <div class="prod-grid">
    <div class="prod"><div class="prod-img" role="img" aria-label="Burgundy stage curtains" style="background:linear-gradient(180deg,#f0f0f0 10%,#8a1a34 12%,#6a1226)"></div>
      <h5>VW Tovra Plain Flame Retardant Curtains | Thermal</h5><div class="stars">★★★★★</div>
      <div class="price"><span>Excl. Tax: £41.67</span><span>Incl. Tax: £50.00</span></div>
      <div class="actions"><span>🛒 Add to Basket</span><span>◉ View Product</span></div></div>
    <div class="prod"><div class="prod-img" role="img" aria-label="Sage blackout fabric beside a headboard" style="background:linear-gradient(90deg,#8a9478,#6a7058 40%,#c8c4b8)"></div>
      <h5>Solace 23 Colours 137cm &amp; 274cm Wide Blackout FR Fabric</h5><div class="stars">★★★★★</div>
      <div class="price"><span>Excl. Tax: £12.50</span><span>Incl. Tax: £15.00</span></div>
      <div class="actions"><span>🛒 Add to Basket</span><span>◉ View Product</span></div></div>
    <div class="prod"><div class="prod-img" role="img" aria-label="Dark blackout roller blind" style="background:linear-gradient(180deg,#3a3a36,#5a5a52 70%,#b8b0a0)"></div>
      <h5>Arcadia FR Blackout Roller Blinds Chain Operated 36 Colours</h5><div class="stars">★★★★★</div>
      <div class="price"><span>Excl. Tax: £49.99</span><span>Incl. Tax: £59.99</span></div>
      <div class="actions"><span>🛒 Add to Basket</span><span>◉ View Product</span></div></div>
    <div class="prod"><div class="prod-img" role="img" aria-label="Navy bedding on a double bed" style="background:linear-gradient(180deg,#8a8aa0,#3a4470 55%,#2a2a3a)"></div>
      <h5>Flame Retardant Bedding BS7175 Navy Single</h5><div class="stars">★★★★★</div>
      <div class="price"><span>Excl. Tax: £6.45</span><span>Incl. Tax: £7.74</span></div>
      <div class="actions"><span>🛒 Add to Basket</span><span>◉ View Product</span></div></div>
  </div>
  <div class="fav-btns"><a class="btn btn-outline">View All</a><a class="btn btn-red">Get Quick Quote!</a></div>
</div></section>

<section class="blog" role="img" aria-label="Living room with lamp and warm curtains">
  <h2>Velcourt Weaves Blog</h2>
  <div class="blog-grid">
    <div class="post"><div class="post-img" role="img" aria-label="Office with roller blinds" style="background:linear-gradient(135deg,#e8e4dc,#a8a094)"></div>
      <h5>Tailoring Your Workspace with Stylish and Functional Office Roller Blinds</h5><small>17 SEPTEMBER, 2023</small></div>
    <div class="post"><div class="post-img" role="img" aria-label="Stack of upholstery fabric swatches" style="background:linear-gradient(135deg,#3a2a1a,#8a5a2a,#2a1a14)"></div>
      <h5 class="red">Utilising High-Quality Contract Upholstery Fabrics for Care Homes</h5><small>10 SEPTEMBER, 2023</small></div>
    <div class="post"><div class="post-img" role="img" aria-label="Dark blackout curtains" style="background:linear-gradient(90deg,#141414,#3a3a3a,#141414)"></div>
      <h5>Revolutionising Hotel Interior Design with Bespoke Blackout Curtains</h5><small>03 SEPTEMBER, 2023</small></div>
  </div>
  <span class="next"><svg width="8" height="8" viewBox="0 0 8 8"><path d="M2 1l3 3-3 3" fill="none" stroke="#fff" stroke-width="1.5"/></svg></span>
  <a class="btn btn-outline">View All</a>
</section>

<section class="faq"><div class="wrap">
  <div class="faq-col">
    <h2>Frequently Asked Questions</h2>
    <div class="q">How to install cubicle tracks on suspended ceilings? <b>+</b></div>
    <div class="q open">What is acoustic absorption? <b>–</b></div>
    <p class="answer">Acoustic absorption refers to the process by which a material, structure, or object takes in sound energy when sound waves are encountered, as opposed to reflecting the energy. Part of the absorbed energy is transformed into heat and part is transmitted through the absorbing body.</p>
    <div class="q">Do I get a certificate to show my products are flame retardant? <b>+</b></div>
    <div class="q">What is curtain fullness &amp; what fullness will my curtains be? <b>+</b></div>
    <a class="btn btn-outline">View All</a>
  </div>
  <form class="contact">
    <h2>Any Questions? Contact Us!</h2>
    <div class="field">First Name</div>
    <div class="field">Last Name</div>
    <div class="field">Your Email</div>
    <div class="field">Phone Number</div>
    <div class="field tall">Comments...</div>
    <div class="agree"><i></i>I agree to having my details collected as per the <u>Privacy Policy</u></div>
    <a class="btn btn-red">Send</a>
  </form>
</div></section>

<footer class="footer" role="img" aria-label="Dark red curtain backdrop">
  <div class="wrap">
    <div class="foot-cols">
      <div class="fcol"><h4>Contact Info</h4>
        <div class="ci"><span class="ic"><svg width="10" height="10" viewBox="0 0 10 10"><path d="M2 1l2 2-1 1.5c.7 1.3 1.2 1.8 2.5 2.5L7 6l2 2-1.5 1.5C4 9 1 6 .5 2.5z" fill="#fff"/></svg></span><span class="red" style="font-size:12px">0117 496 0321</span></div>
        <div class="ci"><span class="ic"><svg width="10" height="8" viewBox="0 0 10 8"><rect x=".5" y=".5" width="9" height="7" fill="none" stroke="#fff"/><path d="M.5.5 5 4.5 9.5.5" fill="none" stroke="#fff"/></svg></span><span>sales@velcourt-weaves.co.uk</span></div>
        <div class="ci"><span class="ic"><svg width="10" height="10" viewBox="0 0 10 10"><circle cx="5" cy="5" r="4" fill="none" stroke="#fff"/><path d="M5 2.5V5h2" fill="none" stroke="#fff"/></svg></span><span>Mon - Fri 9am - 5pm</span></div>
        <div class="ci"><span class="ic"><svg width="8" height="10" viewBox="0 0 8 10"><path d="M4 10S0 5.5 0 4a4 4 0 0 1 8 0c0 1.5-4 6-4 6z" fill="#fff"/></svg></span><span><span class="red">VELCOURT WEAVES</span><br>Unit 7 Mill Lane, Backford, Bristol, BS99 1ZZ<br>United Kingdom</span></div>
      </div>
      <div class="fcol"><h4>Useful Links</h4>
        <ul><li class="red">Home</li><li>About Us</li><li>FAQ's</li><li>Curtain and Blind Installation Nationwide</li><li>How to Measure for Curtains and Blinds</li><li>Blog</li><li>Delivery &amp; Shipping Information</li><li>Client Reviews</li><li>Returns &amp; Cancellation</li><li>Charity</li></ul></div>
      <div class="fcol"><h4>Our Products</h4>
        <ul><li>Flame Retardant Curtains</li><li>Fire Resistant Blinds</li><li>Made to Measure Curtains</li><li>Acoustic Curtains</li><li>Curtain Fabrics</li><li>Curtain Poles</li><li>Curtain Tracks</li></ul></div>
      <div class="fcol">
        <div class="foot-logo"><span class="logo-mark"></span><span class="logo-name">Velcourt Weaves</span></div>
        <h4 style="margin:16px 0 0;font-size:10px">Follow Us:</h4>
        <div class="social"><i></i><i></i><i></i><i class="on"></i><i></i><i></i><i></i></div>
        <a class="btn btn-red" style="font-size:8px">Contact Us</a>
      </div>
    </div>
  </div>
  <div class="bottom"><div class="wrap">
    <span>© 2013-2023 <span class="red">Velcourt Weaves</span>. All Rights Reserved. VAT Number GB000123456</span>
    <span style="margin-left:auto;margin-right:60px">Terms and Conditions &nbsp;|&nbsp; Privacy Policy</span>
    <span class="cards"><span>PayWay</span><span>Cardia</span><span>Mastro</span><span>Bankly</span><span>Cardia</span></span>
  </div></div>
</footer>

</body>
</html>
```